Design some Business Cards

Thank you so much for viewing my contest ! Please be creative
I need some business cards with a cool design, simple and professional.
Below i will add 2 Logos. I want a matte black Background Entry, and a white background entry both front and back. PLEASE KEEP ORIGINAL LOGO COLORS
Please add to the back of the card
Service/Repair/Installations
Duct cleaning services
Miami Dade/Broward County
Call now for a free quote
Special Duct Cleaning Prices
I will need to include contact info for example:
Instagram
Email
Phone Number
Thank you any questions feel free to contact me.!
I appreciate any creative work!

```html
<!DOCTYPE html>
<html lang="en">
<head>
<meta charset="UTF-8">
<title>Cool Current – Business Cards</title>
<link rel="stylesheet" href="https://fonts.googleapis.com/css2?family=Lato:wght@300;400;700;900&display=swap">
<style>
  :root {
    --stage: #8f8f8f;
    --card: #151515;
    --blue: #2f9cc4;
    --red: #e0262b;
    --white: #f2f2f2;
    --muted: #bdbdbd;
  }
  * { margin: 0; padding: 0; box-sizing: border-box; }
  html, body { width: 1200px; height: 900px; overflow: hidden; }
  body {
    background: radial-gradient(circle at 55% 40%, #a9a9a9, var(--stage) 70%);
    font-family: "Lato", sans-serif;
    position: relative;
  }
  .card {
    position: absolute;
    width: 560px;
    height: 320px;
    background: var(--card);
    border-radius: 26px;
    overflow: hidden;
    box-shadow: 0 18px 40px rgba(0,0,0,.35);
    color: var(--white);
  }
  .card--back { left: 580px; top: 100px; }
  .card--front { left: 60px; top: 480px; }

  .brand { display: flex; flex-direction: column; align-items: center; }
  .brand__mark {
    width: 46px; height: 46px; border-radius: 50%;
    border: 4px solid var(--blue);
    margin-bottom: 8px;
  }
  .brand__name {
    font-weight: 900; font-size: 30px; letter-spacing: 1px;
    color: var(--blue); text-transform: uppercase; line-height: 1;
  }
  .brand__tag {
    font-size: 9px; letter-spacing: 4px; color: var(--blue);
    text-transform: uppercase; margin-top: 4px;
  }

  /* back */
  .card--back .brand { position: absolute; top: 34px; left: 0; right: 0; }
  .back__rule { position: absolute; top: 160px; left: 230px; width: 100px; height: 1px; background: var(--red); }
  .services {
    position: absolute; top: 170px; left: 0; right: 0;
    text-align: center; font-size: 12.5px; font-weight: 300; line-height: 1.45; color: var(--white);
  }
  .services__highlight { font-weight: 700; font-size: 15px; }
  .back__stripe { position: absolute; left: 0; right: 0; bottom: 26px; height: 5px; background: var(--blue); }
  .back__band { position: absolute; left: 0; right: 0; bottom: 0; height: 26px; background: var(--red); }

  /* front */
  .card--front .brand { position: absolute; top: 30px; left: 0; right: 0; }
  .front__divider { position: absolute; left: 279px; top: 175px; width: 1px; height: 100px; background: var(--red); }
  .contact {
    position: absolute; right: 295px; top: 180px;
    list-style: none; text-align: right;
  }
  .contact li {
    display: flex; align-items: center; justify-content: flex-end; gap: 12px;
    font-size: 12px; font-weight: 300; height: 26px;
  }
  .contact svg { width: 15px; height: 15px; fill: var(--red); }
  .person { position: absolute; left: 300px; top: 198px; }
  .person__name { font-size: 26px; letter-spacing: 1px; color: var(--blue); font-weight: 400; text-transform: uppercase; }
  .person__name span { font-weight: 300; color: #7fb9d0; }
  .person__role { font-size: 13px; font-weight: 300; margin-top: 2px; }
</style>
</head>
<body>
  <section class="card card--back" aria-label="Card back">
    <div class="brand">
      <div class="brand__mark"></div>
      <div class="brand__name">Cool Current</div>
      <div class="brand__tag">Air Conditioning</div>
    </div>
    <div class="back__rule"></div>
    <p class="services">
      Service | Repair | Installations<br>
      <span class="services__highlight">Duct Cleaning Services</span><br>
      Miami Dade | Broward County<br>
      Call now for a free quote
    </p>
    <div class="back__stripe"></div>
    <div class="back__band"></div>
  </section>

  <section class="card card--front" aria-label="Card front">
    <div class="brand">
      <div class="brand__mark"></div>
      <div class="brand__name">Cool Current</div>
      <div class="brand__tag">Air Conditioning</div>
    </div>
    <ul class="contact">
      <li>(+12) 555 01 2345
        <svg viewBox="0 0 24 24"><path d="M6.6 10.8a15 15 0 0 0 6.6 6.6l2.2-2.2a1 1 0 0 1 1-.25 11 11 0 0 0 3.6.6 1 1 0 0 1 1 1V20a1 1 0 0 1-1 1A17 17 0 0 1 3 4a1 1 0 0 1 1-1h3.5a1 1 0 0 1 1 1 11 11 0 0 0 .6 3.6 1 1 0 0 1-.25 1z"/></svg>
      </li>
      <li>marcoreyes@mail.com
        <svg viewBox="0 0 24 24"><path d="M2 5h20v14H2zm2 2v.4l8 5 8-5V7zm0 2.8V17h16V9.8l-8 5z"/></svg>
      </li>
      <li>coolcurrent_hvac
        <svg viewBox="0 0 24 24"><rect x="3" y="3" width="18" height="18" rx="3"/></svg>
      </li>
    </ul>
    <div class="front__divider"></div>
    <div class="person">
      <div class="person__name">Marco <span>Reyes</span></div>
      <div class="person__role">CEO</div>
    </div>
  </section>
</body>
</html>
```